Create a pitch deck for a specialist physical product development search firm

Please review the attached project brief and the following instructions.
I need a designer to create a 10-slide pitch deck for Vemra, a specialist recruitment partner for physical product design & development companies. The deck will be used to pitch our retained/exclusive recruitment service to potential clients.
The design should:
Follow our bold, clean brand guidelines (provided)
Feel premium, minimalist, and professional
The deck includes:
Problem statement
Our story & differentiators
Process overview
2 client case studies
Social proof/testimonials
Clear call-to-action
Deliverables:
Editable Canva file (preferred) or PowerPoint
Exported PDF
Optional: LinkedIn carousel adaptation
Look and feel
Each slider illustrates characteristics of the customer's brand and the style your logo design should communicate.

```html
<!DOCTYPE html>
<html lang="en">
<head>
<meta charset="utf-8">
<title>Vemra — Pitch Deck Overview</title>
<link href="https://fonts.googleapis.com/css2?family=Poppins:wght@400;500;600;700;800&display=swap" rel="stylesheet">
<style>
:root{
  --page:#e9e9e9;
  --slide:#2b2d33;
  --panel:#3a3834;
  --orange:#f0ac38;
  --orange-deep:#d67a0c;
  --ink:#ffffff;
  --ink-soft:#e4e4e4;
  --dark:#2b2d33;
}
*{box-sizing:border-box;margin:0;padding:0}
html,body{width:1029px;height:1200px;overflow:hidden;background:var(--page)}
body{position:relative;font-family:'Poppins',sans-serif;color:var(--ink)}
.slide{position:absolute;width:458px;height:258px;background:var(--slide);overflow:hidden}
.col-a{left:39px}.col-b{left:533px}
.row-1{top:41px}.row-2{top:328px}.row-3{top:614px}.row-4{top:901px}

.title-tab{position:absolute;left:7px;top:7px;width:293px;height:36px;border-radius:0 18px 0 18px;
  background:linear-gradient(180deg,var(--orange) 0%,var(--orange-deep) 100%);
  font-weight:600;font-size:14.5px;line-height:36px;padding-left:16px;color:#fff}
.subhead{position:absolute;font-weight:600;font-size:7.2px;letter-spacing:.2px;text-transform:uppercase}
.subhead.orange{color:var(--orange)}

.footer-num{position:absolute;left:55px;bottom:0;width:26px;height:26px;border-radius:50%;background:var(--orange);
  color:var(--dark);font-weight:700;font-size:7.5px;line-height:26px;text-align:center;transform:translateY(0)}
.footer-bar{position:absolute;left:91px;bottom:0;width:313px;height:26px;border-radius:13px 13px 0 0;background:var(--orange-deep);
  display:flex;align-items:center;justify-content:center;gap:14px;font-size:6.2px;font-weight:500;color:#fff}
.footer-bar span{display:flex;align-items:center;gap:5px}
.footer-bar svg{width:6px;height:6px}

/* cover */
.cover-graphic{position:absolute;left:0;top:0;width:262px;height:258px;
  background:linear-gradient(135deg,var(--orange) 0%,var(--orange-deep) 100%);border-radius:0 140px 140px 0}
.brand{position:absolute;right:23px;top:34px;display:flex;align-items:center;gap:10px}
.brand-dot{width:26px;height:26px;border-radius:50%;background:var(--orange)}
.brand-name{font-weight:600;font-size:38px;line-height:1;color:#fff}
.cover-title{position:absolute;right:23px;top:124px;text-align:right;font-weight:600;font-size:19px;line-height:26px;color:#fff}
.cover-title .accent{color:var(--orange-deep)}

/* who we help */
.card{position:absolute;top:81px;width:128px;height:126px;border:0.6px solid #8a6a33;border-radius:0 14px 0 0;background:#28292d}
.card-icon{position:absolute;top:7px;left:50%;transform:translateX(-50%);width:26px;height:26px}
.card-label{position:absolute;top:39px;left:0;right:0;height:21px;background:var(--orange);color:var(--dark);
  font-size:6.3px;font-weight:600;text-align:center;line-height:21px}
.card-list{position:absolute;top:71px;left:0;right:0;list-style:none;text-align:center;font-size:6px;line-height:14px;color:var(--ink-soft)}

/* numbered lists */
.num-list{position:absolute;list-style:none}
.num-list li{display:flex;align-items:center}
.num-list .n{color:var(--orange);font-weight:500}
.broken li{height:26.6px;font-size:9.3px}
.broken .n{width:33px}

/* process */
.step{position:absolute;left:24px;display:flex;gap:8px}
.step-dot{width:24px;height:24px;border-radius:50%;background:linear-gradient(180deg,var(--orange),var(--orange-deep));
  color:var(--dark);font-weight:700;font-size:7.5px;line-height:24px;text-align:center;margin-top:2px}
.step h4{font-size:7px;font-weight:600;margin-top:-3px}
.step p{font-size:6.6px;margin-top:5px}
.quote{position:absolute;left:236px;width:198px;height:69px;background:var(--panel);border-radius:0 18px 0 0;padding:9px 0 0 17px}
.quote svg{width:12px;height:10px}
.quote p{font-size:5.6px;line-height:12px;color:var(--ink-soft);margin-top:4px;padding-right:10px}
.quote .by{color:var(--ink-soft);margin-top:0}
.quote .by b{color:var(--orange);font-weight:500}
.stats{position:absolute;left:82px;top:211px;display:flex;gap:9px;font-size:6.7px;color:var(--ink-soft)}
.stats span{display:flex;align-items:center;gap:4px}
.stats svg{width:6px;height:6px}

/* story */
.story-text{position:absolute;left:24px;top:80px;width:194px;font-size:6.2px;line-height:13.5px;text-align:justify;color:var(--ink-soft)}
.story-text p+p{margin-top:7px}
.value{position:absolute;left:250px;width:184px;height:34px;background:var(--panel);border-radius:0 12px 0 0;
  display:flex;align-items:center;gap:12px;padding-left:5px;font-size:6.2px;line-height:12px;color:var(--ink-soft)}
.value-icon{flex:none;width:23px;height:23px;border-radius:50%;background:var(--orange);border-top-left-radius:0;
  display:flex;align-items:center;justify-content:center}
.value-icon svg{width:13px;height:13px}

/* case study */
.case-label{position:absolute;left:0;width:85px;height:23px;background:var(--orange);color:var(--dark);
  font-size:7px;font-weight:600;line-height:23px;padding-left:24px;border-radius:0 12px 12px 0}
.case-line{position:absolute;left:102px;font-size:6.6px;white-space:nowrap}
.case-line .n{color:var(--orange);margin-right:6px}

/* difference */
.diff li{height:20.8px;font-size:7.8px}
.diff .n{width:28px}
.blob{position:absolute;width:27px;height:25px;background:#3d3b37;border-radius:50% 50% 50% 0}
.testimonial{position:absolute;left:56px;top:156px;width:347px;height:58px;background:var(--panel);border-radius:0 0 0 18px}
.portrait{position:absolute;left:10px;top:6px;width:45px;height:45px;border-radius:0 22px 22px 22px;
  background:linear-gradient(160deg,#cfd3d6,#6f8ea4)}
.portrait-badge{position:absolute;left:39px;top:30px;width:22px;height:22px;border-radius:50%;background:var(--orange-deep);
  display:flex;align-items:center;justify-content:center}
.portrait-badge svg{width:10px;height:9px}
.testimonial blockquote{position:absolute;left:82px;top:11px;width:250px;font-size:6.8px;font-weight:700;line-height:13.5px;text-transform:uppercase}
.testimonial .by{position:absolute;left:82px;top:40px;font-size:5.6px;color:var(--ink-soft)}
.testimonial .by b{color:var(--orange);font-weight:500}

/* cta */
.cta-bg{position:absolute;inset:0;background:linear-gradient(160deg,#e79b2a 0%,#f0ac38 55%,#eaa130 100%)}
.cta-mark{position:absolute;left:193px;top:63px;width:72px;height:72px;border-radius:0 50% 50% 50%;background:var(--dark);
  display:flex;align-items:center;justify-content:center}
.cta-mark svg{width:42px;height:34px}
.cta-title{position:absolute;left:0;right:0;top:144px;text-align:center;font-weight:800;font-size:30px;color:var(--dark);letter-spacing:.3px}
.cta-sub{position:absolute;left:0;right:0;top:186px;text-align:center;font-size:7.8px;font-weight:500;color:var(--dark);letter-spacing:.3px}
</style>
</head>
<body>

<!-- Cover -->
<section class="slide col-a row-1">
  <div class="cover-graphic" role="img" aria-label="Large geometric brand graphic in warm orange tones"></div>
  <div class="brand"><span class="brand-dot"></span><span class="brand-name">vemra</span></div>
  <h1 class="cover-title">Specialist Search for<br>Physical Product<br>Design &amp;<br><span class="accent">Development</span></h1>
</section>

<!-- Who We Help -->
<section class="slide col-b row-1">
  <h2 class="title-tab">Who We Help</h2>
  <p class="subhead" style="left:0;right:0;top:59px;text-align:center">Who we help &amp; what success looks like</p>
  <div class="card" style="left:24px">
    <svg class="card-icon" viewBox="0 0 26 26" fill="none" stroke="#f0ac38" stroke-width="0.9"><circle cx="13" cy="15" r="3"/><circle cx="7" cy="16" r="2.4"/><circle cx="19" cy="16" r="2.4"/><path d="M8 24c0-3 2-5 5-5s5 2 5 5M2 24c0-2.5 2-4 5-4M24 24c0-2.5-2-4-5-4"/><path d="M7 6l1 2 2 .3-1.5 1.4.4 2L7 10.8 5.1 11.7l.4-2L4 8.3 6 8zM13 3l1 2 2 .3-1.5 1.4.4 2L13 7.8 11.1 8.7l.4-2L10 5.3 12 5zM19 6l1 2 2 .3-1.5 1.4.4 2L19 10.8l-1.9.9.4-2L16 8.3 18 8z"/></svg>
    <div class="card-label">TYPICAL CLIENTS</div>
    <ul class="card-list"><li>Hardware start-ups &amp; scale-ups</li><li>Design consultancies</li><li>Medtech &amp; consumer health brands</li></ul>
  </div>
  <div class="card" style="left:165px">
    <svg class="card-icon" viewBox="0 0 26 26" fill="none" stroke="#f0ac38" stroke-width="0.9"><circle cx="13" cy="13" r="11"/><circle cx="13" cy="13" r="7.5"/><path d="M13 8a3 3 0 0 1 2 5.3V15h-4v-1.7A3 3 0 0 1 13 8zM11.5 17h3"/></svg>
    <div class="card-label">CHALLENGES</div>
    <ul class="card-list"><li>Long hiring cycles</li><li>Low candidate engagement</li><li>Difficulty finding niche talent</li></ul>
  </div>
  <div class="card" style="left:306px">
    <svg class="card-icon" viewBox="0 0 26 26" fill="none" stroke="#f0ac38" stroke-width="0.9"><circle cx="13" cy="14" r="10"/><circle cx="13" cy="14" r="6.5"/><circle cx="13" cy="14" r="3"/><path d="M13 14l9-9M19 3v3h3"/><circle cx="7" cy="20" r="3"/><path d="M5.7 20l1 1 2-2"/></svg>
    <div class="card-label">WHAT SUCCESS LOOKS LIKE</div>
    <ul class="card-list"><li>Hiring within 3–6 weeks</li><li>Candidates aligned &amp; excited</li><li>Predictable process &amp; higher retention</li></ul>
  </div>
  <div class="footer-num">05</div>
  <div class="footer-bar">
    <span><svg viewBox="0 0 10 10" fill="#fff"><path d="M5 0a3.5 3.5 0 0 0-3.5 3.5C1.5 6 5 10 5 10s3.5-4 3.5-6.5A3.5 3.5 0 0 0 5 0zm0 5a1.4 1.4 0 1 1 0-2.8A1.4 1.4 0 0 1 5 5z"/></svg>14 Harlow Yard, London, UK, EC2A 4LT</span>
    <span><svg viewBox="0 0 10 10" fill="#fff"><path d="M2 0l2 2.5-1 1.2a6 6 0 0 0 3.3 3.3l1.2-1L10 8 8.5 10C4 9.6.4 6 0 1.5z"/></svg>+44 (0)20 7946 0381</span>
  </div>
</section>

<!-- Why Recruitment Feels Broken -->
<section class="slide col-a row-2">
  <h2 class="title-tab">Why Recruitment Feels Broken</h2>
  <ol class="num-list broken" style="left:76px;top:65px">
    <li><span class="n">01)</span>High-volume, transactional models lead to disengagement</li>
    <li><span class="n">02)</span>Lack of true partnership between clients &amp; recruiters</li>
    <li><span class="n">03)</span>Time wasted screening irrelevant CVs</li>
    <li><span class="n">04)</span>Poor candidate journeys = poor hiring outcomes</li>
    <li><span class="n">05)</span>Recruiters who don’t “get” the market or what good looks like</li>
  </ol>
  <div class="footer-num">02</div>
  <div class="footer-bar">
    <span><svg viewBox="0 0 10 10" fill="#fff"><path d="M5 0a3.5 3.5 0 0 0-3.5 3.5C1.5 6 5 10 5 10s3.5-4 3.5-6.5A3.5 3.5 0 0 0 5 0zm0 5a1.4 1.4 0 1 1 0-2.8A1.4 1.4 0 0 1 5 5z"/></svg>14 Harlow Yard, London, UK, EC2A 4LT</span>
    <span><svg viewBox="0 0 10 10" fill="#fff"><path d="M2 0l2 2.5-1 1.2a6 6 0 0 0 3.3 3.3l1.2-1L10 8 8.5 10C4 9.6.4 6 0 1.5z"/></svg>+44 (0)20 7946 0381</span>
  </div>
</section>

<!-- How We Deliver -->
<section class="slide col-b row-2">
  <h2 class="title-tab">How We Deliver</h2>
  <p class="subhead" style="left:24px;top:59px">A partnership-led process that works</p>
  <div class="step" style="top:83px"><div class="step-dot">01</div><div><h4>DEFINE:</h4><p>Understand your business, team culture &amp; goals</p></div></div>
  <div class="step" style="top:126px"><div class="step-dot">02</div><div><h4>ENGAGE:</h4><p>Exclusive, tailored candidate journeys</p></div></div>
  <div class="step" style="top:168px"><div class="step-dot">03</div><div><h4>DELIVER:</h4><p>Predictable outcomes with high engagement</p></div></div>
  <div class="quote" style="top:54px">
    <svg viewBox="0 0 12 10" fill="none" stroke="#f0ac38" stroke-width="0.9"><path d="M1 1h7v5H4L2 8V6H1zM9 3h2v5h-1v1.5L8.5 8H5"/></svg>
    <p>"No agency shenanigans – helped us build a professional hiring experience."</p>
    <p class="by"><b>— Tom Ashworth</b>, Co-Founder, Fieldform Works</p>
  </div>
  <div class="quote" style="top:131px">
    <svg viewBox="0 0 12 10" fill="none" stroke="#f0ac38" stroke-width="0.9"><path d="M1 1h7v5H4L2 8V6H1zM9 3h2v5h-1v1.5L8.5 8H5"/></svg>
    <p>"Compared to other recruiters, this was faster, more personalised, and highly organised."</p>
    <p class="by"><b>— Nina Sorell</b>, CEO, Brightwell Health</p>
  </div>
  <div class="stats">
    <span><svg viewBox="0 0 10 10" fill="none" stroke="#f0ac38" stroke-width="1.2"><rect x="1" y="1" width="8" height="8" rx="1"/><path d="M3 5l1.6 1.6L7.5 3.5"/></svg>100% fill rate</span><span>|</span>
    <span><svg viewBox="0 0 10 10" fill="none" stroke="#f0ac38" stroke-width="1.2"><rect x="1" y="1" width="8" height="8" rx="1"/><path d="M3 5l1.6 1.6L7.5 3.5"/></svg>97% retention after 12 months</span><span>|</span>
    <span><svg viewBox="0 0 10 10" fill="none" stroke="#f0ac38" stroke-width="1.2"><rect x="1" y="1" width="8" height="8" rx="1"/><path d="M3 5l1.6 1.6L7.5 3.5"/></svg>+92 NPS (world-class)</span>
  </div>
  <div class="footer-num">06</div>
  <div class="footer-bar">
    <span><svg viewBox="0 0 10 10" fill="#fff"><path d="M5 0a3.5 3.5 0 0 0-3.5 3.5C1.5 6 5 10 5 10s3.5-4 3.5-6.5A3.5 3.5 0 0 0 5 0zm0 5a1.4 1.4 0 1 1 0-2.8A1.4 1.4 0 0 1 5 5z"/></svg>14 Harlow Yard, London, UK, EC2A 4LT</span>
    <span><svg viewBox="0 0 10 10" fill="#fff"><path d="M2 0l2 2.5-1 1.2a6 6 0 0 0 3.3 3.3l1.2-1L10 8 8.5 10C4 9.6.4 6 0 1.5z"/></svg>+44 (0)20 7946 0381</span>
  </div>
</section>

<!-- The Vemra Story -->
<section class="slide col-a row-3">
  <h2 class="title-tab">The Vemra Story</h2>
  <p class="subhead orange" style="left:24px;top:61px">Vemra means chord. It’s about harmony.</p>
  <div class="story-text">
    <p>Vemra comes from the old word Vemre, meaning chord—a symbol of harmony where individual notes create something greater.</p>
    <p>I founded Vemra to bring this principle into recruitment. Too often, traditional recruitment feels transactional: high volume, low engagement, and little understanding of what makes a team resonate.</p>
    <p>At Vemra, we help hardware brands, consultancies, and medtech innovators build teams that thrive.</p>
  </div>
  <p class="subhead" style="left:250px;top:61px">Vemra is about:</p>
  <div class="value" style="top:82px"><span class="value-icon"><svg viewBox="0 0 14 14" fill="none" stroke="#2b2d33" stroke-width="0.9"><path d="M1 6l3-3 3 2 3-2 3 3-6 6z"/><path d="M5 7l2 2M7 6l2 2"/></svg></span>Relationships over transactions</div>
  <div class="value" style="top:126px"><span class="value-icon"><svg viewBox="0 0 14 14" fill="none" stroke="#2b2d33" stroke-width="0.9"><circle cx="4" cy="6" r="2"/><circle cx="10" cy="6" r="2"/><path d="M1 13c0-2 1.3-3.5 3-3.5S7 11 7 13M7 13c0-2 1.3-3.5 3-3.5s3 1.5 3 3.5M2 1h4v2H2zM8 1h4v2H8z"/></svg></span>Speaking your language, knowing your market</div>
  <div class="value" style="top:170px"><span class="value-icon"><svg viewBox="0 0 14 14" fill="none" stroke="#2b2d33" stroke-width="0.9"><circle cx="5" cy="5" r="2.2"/><path d="M1 13c0-2.5 1.8-4 4-4s4 1.5 4 4M11 2v10M9.5 4h3M9.5 7h3M9.5 10h3"/></svg></span>Creating lasting impact for candidates and clients</div>
  <div class="footer-num">03</div>
  <div class="footer-bar">
    <span><svg viewBox="0 0 10 10" fill="#fff"><path d="M5 0a3.5 3.5 0 0 0-3.5 3.5C1.5 6 5 10 5 10s3.5-4 3.5-6.5A3.5 3.5 0 0 0 5 0zm0 5a1.4 1.4 0 1 1 0-2.8A1.4 1.4 0 0 1 5 5z"/></svg>14 Harlow Yard, London, UK, EC2A 4LT</span>
    <span><svg viewBox="0 0 10 10" fill="#fff"><path d="M2 0l2 2.5-1 1.2a6 6 0 0 0 3.3 3.3l1.2-1L10 8 8.5 10C4 9.6.4 6 0 1.5z"/></svg>+44 (0)20 7946 0381</span>
  </div>
</section>

<!-- Case Study -->
<section class="slide col-b row-3">
  <h2 class="title-tab">Case Study: Brightwell Health</h2>
  <div class="case-label" style="top:66px">CHALLENGE:</div>
  <p class="case-line" style="top:67px"><span class="n">01)</span>Critical leadership hire during a period of disruption</p>
  <p class="case-line" style="top:85px"><span class="n">02)</span>Lack of trust in recruiters due to previous poor experiences</p>
  <p class="case-line" style="top:103px"><span class="n">03)</span>Limited hiring budget and an unsettled team</p>
  <div class="case-label" style="top:129px">SOLUTION:</div>
  <p class="case-line" style="top:130px"><span class="n">»</span>Founder-led, transparent process to build trust</p>
  <p class="case-line" style="top:148px"><span class="n">»</span>4 candidates shortlisted in 2 weeks</p>
  <p class="case-line" style="top:166px"><span class="n">»</span>Offer accepted within 4.5 weeks</p>
  <div class="case-label" style="top:190px">OUTCOME:</div>
  <p class="case-line" style="top:196px">Secured a CPO who launched Brightwell’s customer-ready product and stabilised the leadership team.</p>
  <div class="footer-num">07</div>
  <div class="footer-bar">
    <span><svg viewBox="0 0 10 10" fill="#fff"><path d="M5 0a3.5 3.5 0 0 0-3.5 3.5C1.5 6 5 10 5 10s3.5-4 3.5-6.5A3.5 3.5 0 0 0 5 0zm0 5a1.4 1.4 0 1 1 0-2.8A1.4 1.4 0 0 1 5 5z"/></svg>14 Harlow Yard, London, UK, EC2A 4LT</span>
    <span><svg viewBox="0 0 10 10" fill="#fff"><path d="M2 0l2 2.5-1 1.2a6 6 0 0 0 3.3 3.3l1.2-1L10 8 8.5 10C4 9.6.4 6 0 1.5z"/></svg>+44 (0)20 7946 0381</span>
  </div>
</section>

<!-- The Vemra Difference -->
<section class="slide col-a row-4">
  <h2 class="title-tab">The Vemra Difference</h2>
  <p class="subhead orange" style="left:24px;top:62px">What makes Vemra different?</p>
  <ol class="num-list diff" style="left:166px;top:57px">
    <li><span class="n">01)</span>Specialist in physical product development roles</li>
    <li><span class="n">02)</span>Founder-led, relationship-first search</li>
    <li><span class="n">03)</span>Boutique, agile, and quality-focused</li>
    <li><span class="n">04)</span>Proven results: faster hiring and better retention</li>
  </ol>
  <div class="blob" style="left:25px;top:130px"></div>
  <div class="blob" style="left:395px;top:218px;border-radius:50% 0 50% 50%"></div>
  <div class="testimonial">
    <div class="portrait" role="img" aria-label="Portrait photo of the quoted client"></div>
    <div class="portrait-badge"><svg viewBox="0 0 12 10" fill="none" stroke="#fff" stroke-width="1"><path d="M1 1h7v5H4L2 8V6H1zM9 3h2v5h-1v1.5L8.5 8H5"/></svg></div>
    <blockquote>We spent a lot less time reviewing CVs as every candidate was spot on.</blockquote>
    <p class="by"><b>- Sam Prentice</b>, Head of Engineering, Velocore</p>
  </div>
  <div class="footer-num">04</div>
  <div class="footer-bar">
    <span><svg viewBox="0 0 10 10" fill="#fff"><path d="M5 0a3.5 3.5 0 0 0-3.5 3.5C1.5 6 5 10 5 10s3.5-4 3.5-6.5A3.5 3.5 0 0 0 5 0zm0 5a1.4 1.4 0 1 1 0-2.8A1.4 1.4 0 0 1 5 5z"/></svg>14 Harlow Yard, London, UK, EC2A 4LT</span>
    <span><svg viewBox="0 0 10 10" fill="#fff"><path d="M2 0l2 2.5-1 1.2a6 6 0 0 0 3.3 3.3l1.2-1L10 8 8.5 10C4 9.6.4 6 0 1.5z"/></svg>+44 (0)20 7946 0381</span>
  </div>
</section>

<!-- Call to action -->
<section class="slide col-b row-4">
  <div class="cta-bg" role="img" aria-label="Orange-toned photo of a modern office workspace"></div>
  <div class="cta-mark"><svg viewBox="0 0 42 34" fill="none" stroke="#f0ac38" stroke-width="1.4"><circle cx="21" cy="12" r="4"/><circle cx="10" cy="8" r="3"/><circle cx="32" cy="8" r="3"/><path d="M13 26c0-5 3.5-8 8-8s8 3 8 8M4 22c0-4 2.5-6.5 6-6.5M38 22c0-4-2.5-6.5-6-6.5"/><circle cx="25" cy="24" r="4"/><path d="M28 27l5 5"/></svg></div>
  <h2 class="cta-title">READY TO HIRE?</h2>
  <p class="cta-sub">LET’S BUILD YOUR NEXT GREAT TEAM TOGETHER.</p>
</section>

</body>
</html>
```